BRAMLEIGH real estate family office

Hello, Our business is a real estate intermediation activity on high-end goods (amounts exceeding € 10m) for corporate and private clients. You can see our logo on the site www.bramleigh-invented.fr We would like to keep that spirit with the hexagon that represents France (transactions between Monaco and Saint Tropez, Courchevel and Paris). And the "baseline" that is "real estate family office". The corporate logo should be and can be printed by embossing (relief). We must integrate the name, first name, phone, email and website. Finally, to imbibe the spirit of business, here is a detail of the activity. "Genuine consulting firm in real estate investments, BRAMLEIGH works with its customers as a specialized player in the high-end markets, we are recognized for our ultra-confidential approach and tailor-made, as well as the quality of our network. We broadcast any information on the market and we work exclusively through a strong relationship we have developed over the years. BRAMLEIGH is active on the French Riviera (from Monaco to Saint-Tropez), the Alps (Courchevel, Méribel, Megève) and Paris (essentially market premium). Always looking for opportunities for our clients, we work on two investment areas: residential luxury real estate (properties, vineyards, mansions, land, etc.) commercial real estate (empty office buildings or yield, hotel properties, land, etc.) "

Target Market(s)

High foreign end customers. corporate and private.

Industry/Entity Type

Real Estate

Contact Information for Business Card

LOGO
baseline
Laurent Dufossé
+33(0)6.41.57.09.64
ld@bramleigh-invented.fr
www.bramleigh-invented.fr

Font styles to use
Serif

Colors
cedeed
0255a3
3277b5
85abd2
85cae6
34a7d7
0792cd
cfdeed
1b1b1b

Requirements
Must have
• see description

```html
<!DOCTYPE html>
<html lang="en">
<head>
<meta charset="utf-8">
<title>Bramleigh – Business Card</title>
<link rel="stylesheet" href="https://fonts.googleapis.com/css2?family=Source+Sans+3:wght@400;600&display=swap">
<style>
  :root {
    --page-bg: #e6eaef;
    --card-top: #f5f6f8;
    --brand-blue: #0b4c9c;
    --brand-blue-light: #2f66b0;
    --text-dark: #1b1b1b;
    --white: #ffffff;
  }
  * { margin: 0; padding: 0; box-sizing: border-box; }
  html, body {
    width: 1200px;
    height: 900px;
    overflow: hidden;
    background: var(--page-bg);
    font-family: "Source Sans 3", sans-serif;
  }
  .stage {
    width: 1200px;
    height: 900px;
    display: flex;
    align-items: center;
    justify-content: center;
  }
  .business-card {
    position: relative;
    width: 900px;
    height: 540px;
    border-radius: 22px;
    overflow: hidden;
    background: var(--card-top);
    box-shadow: 0 14px 40px rgba(20, 40, 80, 0.18);
  }
  .brand {
    position: absolute;
    top: 86px;
    left: 0;
    width: 100%;
    text-align: center;
  }
  .brand-name {
    font-size: 52px;
    font-weight: 600;
    letter-spacing: 1px;
    line-height: 1;
    color: var(--brand-blue);
  }
  .brand-baseline {
    margin-top: 10px;
    font-size: 20px;
    font-weight: 400;
    color: var(--text-dark);
  }
  .roof-band {
    position: absolute;
    left: 0;
    top: 0;
    width: 900px;
    height: 540px;
  }
  .contact {
    position: absolute;
    left: 0;
    top: 318px;
    width: 100%;
    text-align: center;
    color: var(--white);
  }
  .contact-name {
    font-size: 30px;
    font-weight: 600;
    letter-spacing: 0.3px;
    text-transform: uppercase;
  }
  .contact-icons {
    display: flex;
    justify-content: center;
    gap: 14px;
    margin-top: 20px;
    height: 18px;
  }
  .contact-icons svg { width: 18px; height: 18px; fill: var(--white); }
  .contact-lines {
    margin-top: 10px;
    font-size: 23px;
    font-weight: 400;
    line-height: 34px;
  }
</style>
</head>
<body>
<main class="stage">
  <section class="business-card" aria-label="Bramleigh business card">
    <svg class="roof-band" viewBox="0 0 900 540" aria-hidden="true">
      <defs>
        <linearGradient id="bandGradient" x1="0" y1="0" x2="1" y2="1">
          <stop offset="0" stop-color="#2f66b0"/>
          <stop offset="1" stop-color="#0b4c9c"/>
        </linearGradient>
      </defs>
      <polygon points="0,374 450,222 900,371 900,540 0,540" fill="url(#bandGradient)"/>
    </svg>

    <header class="brand">
      <div class="brand-name">BRAMLEIGH</div>
      <div class="brand-baseline">real estate family office</div>
    </header>

    <div class="contact">
      <div class="contact-name">Laurent Dufossé</div>
      <div class="contact-icons">
        <svg viewBox="0 0 24 24" aria-label="Phone"><path d="M3 9c0-3 4-5 9-5s9 2 9 5v2h-5V8.5c-1.2-.4-2.6-.6-4-.6s-2.8.2-4 .6V11H3z"/><path d="M6 12h12l2 8H4z"/></svg>
        <svg viewBox="0 0 24 24" aria-label="Email"><path d="M2 5h20v14H2z M3.5 6.5 12 13l8.5-6.5" stroke="#0b4c9c" stroke-width="1.6"/></svg>
        <svg viewBox="0 0 24 24" aria-label="Website"><circle cx="12" cy="12" r="10"/><path d="M2 12h20M12 2c3 3 3 17 0 20M12 2c-3 3-3 17 0 20" stroke="#0b4c9c" stroke-width="1.6" fill="none"/></svg>
      </div>
      <div class="contact-lines">
        <div class="contact-phone">+33(0)6.41.57.09.64</div>
        <div class="contact-email">ld@bramleigh-invented.fr</div>
        <div class="contact-web">www.bramleigh-invented.fr</div>
      </div>
    </div>
  </section>
</main>
</body>
</html>
```